business card for a massage therapy practice named 'Meadow and Willow Massage Studio'

I really need a trendy, yet easy on the eyes business card to complement my logo. Ideally with some gold or rose gold foil work.

My uploaded file of the logo I have in horizontal but I have a vertical version as well. Another color that is used in the website is a blush pink here and there. I'd like to see some trendy tropical leaves in the design.

```html
<!DOCTYPE html>
<html lang="en">
<head>
<meta charset="utf-8">
<title>Meadow and Willow Massage Studio – Business Card</title>
<link href="https://fonts.googleapis.com/css2?family=Roboto:wght@400;500&display=swap" rel="stylesheet">
<style>
  :root {
    --backdrop: #e4e2de;
    --card: #f6f5f2;
    --card-edge: #e9e7e2;
    --copper: #c5874f;
    --copper-soft: #d3a273;
    --shadow: rgba(60, 55, 48, 0.18);
  }
  * { box-sizing: border-box; margin: 0; padding: 0; }
  html, body {
    width: 1200px;
    height: 900px;
    overflow: hidden;
  }
  body {
    background: var(--backdrop);
    font-family: "Roboto", Arial, sans-serif;
    display: flex;
    flex-direction: column;
    align-items: center;
    justify-content: center;
    gap: 56px;
  }
  .card {
    width: 560px;
    height: 320px;
    background: linear-gradient(160deg, var(--card) 0%, var(--card-edge) 100%);
    box-shadow: 0 14px 34px var(--shadow), 0 2px 4px var(--shadow);
    display: flex;
    align-items: center;
    justify-content: center;
  }
  .card-logo-side .brand {
    display: flex;
    align-items: center;
    gap: 18px;
  }
  .brand-dot {
    width: 46px;
    height: 46px;
    border-radius: 50%;
    background: var(--copper-soft);
  }
  .brand-name {
    color: var(--copper);
    font-weight: 400;
    font-size: 26px;
    line-height: 1.25;
    letter-spacing: 0.5px;
  }
  .card-info-side .contact {
    text-align: center;
    color: var(--copper);
    font-weight: 400;
    font-size: 17px;
    line-height: 1.28;
  }
  .contact .person-name {
    font-weight: 500;
    font-size: 24px;
    line-height: 1.2;
  }
  .contact .person-role { margin-bottom: 14px; }
  .contact .address { margin-bottom: 14px; }
</style>
</head>
<body>
  <section class="card card-logo-side">
    <div class="brand">
      <span class="brand-dot"></span>
      <span class="brand-name">Meadow and Willow<br>Massage Studio</span>
    </div>
  </section>

  <section class="card card-info-side">
    <div class="contact">
      <p class="person-name">Elena Marsh</p>
      <p class="person-role">Massage Therapist</p>
      <p class="address">482 Linden Ave #210<br>Fairview, CA 95000</p>
      <p class="phone">P. (555) 214-7830</p>
      <p class="email">info@meadowandwillow.com</p>
      <p class="web">www.meadowandwillow.com</p>
    </div>
  </section>
</body>
</html>
```